Adventurous female pilot

I am looking for a personal business card, for a very well qualified female pilot, with a lot of aviation experience.

Currently an airline pilot, have worked as a bush pilot in Africa, looking to get into corporate aviation, or private jet owners.
Want a classy looking card for networking...

Could be interested in a retro\vintage look also?!

An idea,, is an african sunset background, with my wings\logo on it
Updates

I just want to say thank you to all of your for your amazing designs!

I have been very busy flying this past week , so not had a chance to be on the computer much.
But I provide some feedback, and conclusions very soon!
Thank you again.

Marla

Reason: Still waiting on a couple of revisions to be 100% about my choice!

Target Market(s)

corporate aviation, private jet owners, casino's,
General audience.
networking

Industry/Entity Type

Airline

Requirements
Nice to have
• Classy, edgy, sexy, but also feminine

```html
<!DOCTYPE html>
<html lang="en">
<head>
<meta charset="utf-8">
<title>Marla Hollis Aviation – Business Card</title>
<link href="https://fonts.googleapis.com/css2?family=Jost:wght@300;400;500&display=swap" rel="stylesheet">
<style>
  :root {
    --page-bg: #cfcfd1;
    --card-edge: #e4e4e6;
    --wine-top: #86002e;
    --wine-mid: #a8004a;
    --wine-low: #6e0033;
    --wine-deep: #45001e;
    --arc-silver: #bdbec2;
    --mark-ink: #4a4a4e;
    --text-white: #ffffff;
    --text-blush: #e6bfd0;
  }
  html, body {
    margin: 0;
    width: 1200px;
    height: 800px;
    overflow: hidden;
    background: var(--page-bg);
    font-family: "Jost", "Futura", sans-serif;
  }
  .business-card {
    position: absolute;
    left: 72px;
    top: 76px;
    width: 1056px;
    height: 646px;
    box-sizing: border-box;
    border: 3px solid var(--card-edge);
    overflow: hidden;
    background: linear-gradient(to bottom,
      var(--wine-top) 0%,
      var(--wine-mid) 32%,
      var(--wine-low) 70%,
      var(--wine-deep) 100%);
  }
  .silver-arc {
    position: absolute;
    left: 0;
    top: 0;
    width: 1050px;
    height: 270px;
  }
  .wings-mark {
    position: absolute;
    left: 0;
    right: 0;
    top: 100px;
    display: flex;
    justify-content: center;
    align-items: center;
    gap: 14px;
    color: var(--mark-ink);
    font-weight: 500;
    font-size: 30px;
    letter-spacing: 6px;
  }
  .wings-mark .mark-dot {
    width: 22px;
    height: 22px;
    border-radius: 50%;
    background: var(--mark-ink);
  }
  .identity {
    position: absolute;
    left: 0;
    right: 0;
    top: 296px;
    text-align: center;
  }
  .identity .person-name {
    margin: 0;
    color: var(--text-white);
    font-weight: 400;
    font-size: 42px;
    letter-spacing: 1.5px;
    line-height: 1.1;
  }
  .identity .profession {
    margin: 4px 0 0;
    color: var(--text-blush);
    font-weight: 400;
    font-size: 28px;
    letter-spacing: 1.5px;
    line-height: 1.1;
  }
  .contact-list {
    position: absolute;
    right: 40px;
    top: 488px;
    margin: 0;
    display: grid;
    grid-template-columns: auto auto;
    column-gap: 30px;
    row-gap: 6px;
    color: var(--text-white);
    font-size: 33px;
    line-height: 40px;
  }
  .contact-list dt {
    font-weight: 300;
    text-align: right;
  }
  .contact-list dd {
    margin: 0;
    font-weight: 400;
    text-align: right;
  }
</style>
</head>
<body>
  <section class="business-card">
    <svg class="silver-arc" viewBox="0 0 1050 270" preserveAspectRatio="none" aria-hidden="true">
      <path d="M0,0 Q525,532 1050,0 Z" fill="var(--arc-silver)"/>
    </svg>

    <div class="wings-mark">
      <span class="mark-dot"></span>
      <span>MARLA HOLLIS</span>
    </div>

    <header class="identity">
      <h1 class="person-name">MARLA HOLLIS</h1>
      <p class="profession">AVIATION</p>
    </header>

    <dl class="contact-list">
      <dt>Cell US:</dt><dd>+1 702-555-0143</dd>
      <dt>Cell Taipei:</dt><dd>+886 970-000-418</dd>
      <dt>e-mail:</dt><dd>marlachollis@example.com</dd>
    </dl>
  </section>
</body>
</html>
```